Bref créative
Logo for a homebuyer business
Brightkey Dwellings Homebuyers
Use same font as used in my logo
Miriam Colby
Co-Owner
xxxxx
BrightKeyDwellings@mailbox-example.net
BrightKeyDwellings.example

```html
<!DOCTYPE html>
<html lang="en">
<head>
<meta charset="utf-8">
<title>Brightkey Dwellings Homebuyers – Stationery</title>
<link href="https://fonts.googleapis.com/css2?family=Cinzel:wght@500&family=Open+Sans:wght@400;600&display=swap" rel="stylesheet">
<style>
  :root {
    --blue: #2c3a9e;
    --brown: #9a6a3d;
    --paper: #ffffff;
    --backdrop: #eceded;
    --ink: #3a3a44;
    --faint: #e6e8f1;
  }
  * { margin: 0; padding: 0; box-sizing: border-box; }
  html, body { width: 1200px; height: 936px; overflow: hidden; background: var(--backdrop); }
  .canvas { position: relative; width: 1200px; height: 936px; font-family: "Open Sans", sans-serif; color: var(--ink); }

  .sheet {
    position: absolute;
    background: linear-gradient(90deg, var(--blue) 50%, var(--brown) 50%);
    box-shadow: 0 2px 6px rgba(0,0,0,.12);
  }
  .sheet-inner { position: absolute; background: var(--paper); }

  .brand {
    font-family: "Cinzel", serif;
    font-weight: 500;
    color: var(--blue);
    line-height: 1.15;
    letter-spacing: .02em;
  }
  .brand-mark { display: inline-block; background: var(--blue); vertical-align: middle; }

  .web { position: absolute; font-size: 10px; font-weight: 600; font-style: italic; color: var(--ink); letter-spacing: .04em; }
  .contact { position: absolute; font-size: 7px; line-height: 1.55; color: var(--ink); }

  /* Letterhead */
  .letterhead { left: 182px; top: 68px; width: 390px; height: 547px; }
  .letterhead .sheet-inner { left: 7px; top: 7px; right: 7px; bottom: 7px; }
  .letterhead .brand { position: absolute; left: 20px; top: 18px; font-size: 11px; }
  .letterhead .contact { right: 18px; top: 42px; }
  .letterhead .watermark { position: absolute; left: 0; right: 0; top: 205px; text-align: center; font-size: 30px; color: var(--faint); }
  .letterhead .web { right: 18px; bottom: 14px; font-size: 8px; }

  /* Folder */
  .folder { left: 633px; top: 43px; width: 455px; height: 582px; }
  .folder .sheet-inner { left: 12px; top: 12px; right: 12px; bottom: 12px; }
  .folder .brand { position: absolute; left: 0; right: 0; top: 238px; text-align: center; font-size: 22px; }
  .folder .brand-mark { width: 14px; height: 14px; margin-bottom: 12px; }
  .folder .web { left: 0; right: 0; bottom: 30px; text-align: center; font-size: 11px; }

  /* Business cards */
  .card { left: 46px; width: 177px; height: 100px; }
  .card .sheet-inner { left: 3px; top: 3px; right: 3px; bottom: 3px; }
  .card-front { top: 655px; }
  .card-back { top: 772px; }
  .card-front .brand { position: absolute; left: 10px; top: 12px; font-size: 7px; width: 70px; }
  .card-front .person { position: absolute; left: 88px; top: 12px; font-size: 6px; line-height: 1.5; }
  .card-front .person strong { font-size: 7px; color: var(--blue); font-weight: 600; }
  .card-front .contact { left: 10px; bottom: 8px; font-size: 5px; }
  .card-back .brand { position: absolute; left: 0; right: 0; top: 26px; text-align: center; font-size: 9px; }
  .card-back .web { left: 0; right: 0; bottom: 10px; text-align: center; font-size: 6px; }

  /* Small envelope */
  .envelope { left: 268px; top: 670px; width: 425px; height: 203px; }
  .envelope .sheet-inner { left: 6px; top: 6px; right: 6px; bottom: 6px; }
  .envelope .brand { position: absolute; left: 46px; top: 14px; font-size: 11px; }
  .envelope .contact { left: 46px; top: 60px; }

  /* Envelope back */
  .envelope-back { position: absolute; left: 734px; top: 665px; width: 430px; height: 208px; box-shadow: 0 2px 6px rgba(0,0,0,.12); }
  .envelope-back .web { left: 0; right: 0; top: 18px; text-align: center; color: #fff; font-size: 8px; }
</style>
</head>
<body>
<div class="canvas">

  <section class="sheet letterhead" aria-label="Letterhead">
    <div class="sheet-inner">
      <div class="brand">Brightkey Dwellings<br>Homebuyers</div>
      <div class="contact">P.O. Box 482 Alder, NY 10001<br>(555) 014-2290<br>BrightKeyDwellings@mailbox-example.net</div>
      <div class="brand watermark">Brightkey Dwellings</div>
      <div class="web">www.BrightKeyDwellings.example</div>
    </div>
  </section>

  <section class="sheet folder" aria-label="Presentation folder">
    <div class="sheet-inner">
      <div class="brand"><span class="brand-mark"></span><br>Brightkey Dwellings<br>Homebuyers</div>
      <div class="web">www.BrightKeyDwellings.example</div>
    </div>
  </section>

  <section class="sheet card card-front" aria-label="Business card front">
    <div class="sheet-inner">
      <div class="brand">Brightkey Dwellings Homebuyers</div>
      <div class="person"><strong>Miriam Colby</strong><br>Co-Owner<br>xxxxx</div>
      <div class="contact">BrightKeyDwellings@mailbox-example.net<br>BrightKeyDwellings.example</div>
    </div>
  </section>

  <section class="sheet card card-back" aria-label="Business card back">
    <div class="sheet-inner">
      <div class="brand">Brightkey Dwellings<br>Homebuyers</div>
      <div class="web">www.BrightKeyDwellings.example</div>
    </div>
  </section>

  <section class="sheet envelope" aria-label="Envelope front">
    <div class="sheet-inner">
      <div class="brand">Brightkey Dwellings<br>Homebuyers</div>
      <div class="contact">P.O. Box 482 Alder, NY 10001</div>
    </div>
  </section>

  <section class="envelope-back" aria-label="Envelope back">
    <svg width="430" height="208" viewBox="0 0 430 208">
      <rect width="430" height="208" fill="#fff"/>
      <path d="M0 0 H430 V30 Q215 85 0 30 Z" fill="var(--blue)"/>
      <rect x="424" y="0" width="6" height="208" fill="var(--brown)"/>
    </svg>
    <div class="web">www.BrightKeyDwellings.example</div>
  </section>

</div>
</body>
</html>
```